SME Business Bookkeeping Brochure

Fully qualified CPA & registered BAS Agent based in Melbourne Australia trading as Larkfield Office Partners looking for a brochure design to help grow my online bookkeeping business. I work together with clients to streamline their systems and procedures and provide help and support for growing their business. Specialising in set up and training of accounting packages and ongoing upkeep of accounts and administration needs. Would like to see colours to compliment logo attached should communicate working together and financial safety and growth

Industry/Entity Type

Business Service

Requirements
Must have
• Complimentary to website: http://www.larkfieldofficepartners.com.au/

```html
<!DOCTYPE html>
<html lang="en">
<head>
<meta charset="utf-8">
<title>Larkfield Office Partners – Bookkeeping Brochure</title>
<link rel="stylesheet" href="https://fonts.googleapis.com/css2?family=Comic+Neue:wght@400;700&family=Lato:wght@400;700&family=Oswald:wght@700&display=swap">
<style>
  :root{
    --purple:#5b3a9c;
    --purple-deep:#4e2f8c;
    --teal:#1fa08c;
    --grey-band:#c9cacd;
    --grey-page:#e4e5e8;
    --ink:#1d1d1f;
    --white:#ffffff;
    --canvas:#f2f2f3;
  }
  *{box-sizing:border-box;margin:0;padding:0}
  html,body{width:1200px;height:1029px;overflow:hidden;background:var(--canvas)}
  .spread{position:absolute;left:20px;top:100px;width:1160px;height:826px;background:var(--white);box-shadow:0 6px 24px rgba(0,0,0,.12)}
  .page{position:absolute;top:0;height:826px;overflow:hidden}
  .page-left{left:0;width:581px;background:linear-gradient(180deg,#d9dadd 0%,#eeeff1 22%,#ffffff 48%,#f4f4f5 69%)}
  .page-right{left:581px;width:579px;background:var(--white)}

  .map-art{position:absolute;left:0;top:0;width:581px;height:190px;background:radial-gradient(ellipse at 55% 35%,rgba(255,255,255,.9) 0%,rgba(220,221,224,.6) 45%,rgba(210,211,214,0) 80%)}
  .about-title{position:absolute;left:30px;top:156px;font:700 24px/1 "Comic Neue",cursive;color:var(--purple);letter-spacing:.5px}
  .about-body{position:absolute;left:32px;top:196px;width:508px;font:400 12.6px/16.2px "Lato",sans-serif;color:var(--ink);text-align:justify}
  .about-body strong{font-weight:700}

  .rule-purple{position:absolute;height:5px;background:var(--purple)}
  .rule-teal{position:absolute;background:var(--teal)}

  .contact-zone{position:absolute;left:0;top:579px;width:581px;height:218px;background:radial-gradient(ellipse at 40% 40%,#d6d7da 0%,var(--grey-band) 70%)}
  .contact-brand{position:absolute;left:30px;top:134px;font:400 16px/1 "Comic Neue",cursive;color:var(--white)}
  .contact-title{position:absolute;left:295px;top:58px;font:700 22px/1 "Comic Neue",cursive;color:var(--purple)}
  .contact-list{position:absolute;left:295px;top:88px;list-style:none}
  .contact-list li{display:flex;align-items:center;gap:5px;height:23px;font:400 13px/1 "Lato",sans-serif;color:var(--white)}
  .contact-list svg{width:10px;height:10px;flex:none}

  .brand-name{position:absolute;left:0;width:579px;top:118px;text-align:center;font:400 26px/1 "Comic Neue",cursive;color:var(--purple)}
  .hero-photo{position:absolute;left:0;top:214px;width:579px;height:353px;background:radial-gradient(ellipse at 62% 45%,#a9aeb2 0%,#6f767c 45%,#3e4449 100%)}
  .headline{position:absolute;right:48px;top:638px;text-align:right}
  .headline h1{font:700 54px/1 "Oswald",sans-serif;color:var(--purple-deep);letter-spacing:.5px}
  .headline p{margin-top:4px;font:400 20px/1 "Comic Neue",cursive;color:var(--ink);letter-spacing:.6px}

  .footer-bands{position:absolute;left:0;top:764px;width:1160px;height:62px}
  .site-url{position:absolute;left:798px;top:782px;width:340px;text-align:right;font:400 16px/1 "Lato",sans-serif;letter-spacing:2.4px;color:var(--ink)}
</style>
</head>
<body>
<div class="spread">
  <section class="page page-left">
    <div class="map-art" role="img" aria-label="Faint world map with network nodes and chat bubble icons"></div>
    <h2 class="about-title">ABOUT US</h2>
    <div class="about-body">
      <p><strong>Larkfield Office Partners proudly taking your stress away by providing expertly managed Bookkeeping Services.</strong></p>
      <p>Larkfield Office Partners began in February 2011 as a part time business and has gone from strength to strength ever since. Maren started the business on her own taking care of simple bookkeeping responsibilities and Registered BAS Agent services for a few small clients while working as a full time Finance Manager for an industry leading IT company.</p>
      <p>At Larkfield Office Partners we pride ourselves on excellence and providing services to support you in both the day to day operations as well as reporting and analysis to improve your decision making abilities. We can provide your business with all necessary reports and information to assist and ensure the success and growth of your business.</p>
      <p>The expertise of our bookkeeping services will support you in reaching your businesses full potential. Partnering with us will help free up your time, allowing you to work on growing the business you love rather than using valuable time, energy and lost opportunities working on the nitty gritty day to day grind.</p>
      <p>A full detailed list of services can be found on our services page.</p>
      <p>Talk to Larkfield Office Partners today and start running your business…</p>
      <p>THE STRESS FREE WAY! Contact us today for a free, no obligation, initial consultation so we can discuss what is best for your needs.</p>
    </div>
    <div class="rule-purple" style="left:0;top:574px;width:581px"></div>
    <div class="contact-zone">
      <div class="contact-brand">Larkfield Office Partners</div>
      <h3 class="contact-title">CONTACT</h3>
      <ul class="contact-list">
        <li><svg viewBox="0 0 10 10"><path d="M5 0a3.5 3.5 0 0 0-3.5 3.5C1.5 6 5 10 5 10s3.5-4 3.5-6.5A3.5 3.5 0 0 0 5 0zm0 5a1.5 1.5 0 1 1 0-3 1.5 1.5 0 0 1 0 3z" fill="#5b3a9c"/></svg>14 Ashgrove Lane, Brindle VIC 3071</li>
        <li><svg viewBox="0 0 10 10"><path d="M2 0.5l2 2-1 1.2c.6 1.3 1.6 2.3 2.9 2.9L7 5.6l2 2-1.2 1.6C4 9 1 6 .6 2.2z" fill="#5b3a9c"/></svg>+61 0400 555 218</li>
        <li><svg viewBox="0 0 10 10"><rect x="0.5" y="2" width="9" height="6.5" fill="#5b3a9c"/><path d="M0.5 2L5 5.5 9.5 2" stroke="#fff" stroke-width=".8" fill="none"/></svg>maren@larkfieldofficepartners.com.au</li>
        <li><svg viewBox="0 0 10 10"><circle cx="5" cy="5" r="4.3" fill="#5b3a9c"/><path d="M.7 5h8.6M5 .7c-2 2.5-2 6.1 0 8.6M5 .7c2 2.5 2 6.1 0 8.6" stroke="#fff" stroke-width=".6" fill="none"/></svg>www.larkfieldofficepartners.com.au</li>
      </ul>
    </div>
  </section>

  <section class="page page-right">
    <div class="brand-name">Larkfield Office Partners</div>
    <div class="rule-teal" style="left:238px;top:189px;width:341px;height:14px"></div>
    <div class="rule-purple" style="left:0;top:203px;width:579px"></div>
    <div class="hero-photo" role="img" aria-label="Businessman in a suit touching a glowing cloud icon surrounded by device and email icons"></div>
    <div class="rule-purple" style="left:0;top:571px;width:579px;height:6px"></div>
    <div class="rule-teal" style="left:238px;top:577px;width:341px;height:18px"></div>
    <div class="headline">
      <h1>THE COMPLETE ANSWER</h1>
      <p>TO ALL OF YOUR BOOKKEEPING WANTS AND NEEDS</p>
    </div>
  </section>

  <svg class="footer-bands" viewBox="0 0 1160 62" aria-hidden="true">
    <polygon points="0,33 747,33 726,62 0,62" fill="#1fa08c"/>
    <polygon points="726,62 780,0 1160,0 1160,62" fill="#c9cacd"/>
  </svg>
  <div class="site-url">www.larkfieldofficepartners.com.au</div>
</div>
</body>
</html>
```